Construction Company Business Card

Business Card Design using new Logo

Contact Information for Business Card

include all company info and website

Requirements
Must have
• Wesley Corman - President
ph. 254-617-0382
Cedar Knoll, TX
wesley@ironmarkframing.com
www.ironmarkframing.com

```html
<!DOCTYPE html>
<html lang="en">
<head>
<meta charset="utf-8">
<title>Ironmark Framing Texas – Business Card</title>
<link rel="stylesheet" href="https://fonts.googleapis.com/css2?family=Arimo:wght@400;700&display=swap">
<style>
  :root {
    --bg: #2a2a2a;
    --card: #0b0b0b;
    --card-edge: #161616;
    --red: #d7262e;
    --white: #f2f2f2;
    --muted: #c9c9c9;
    --star: #262626;
  }
  * { margin: 0; padding: 0; box-sizing: border-box; }
  html, body { width: 1200px; height: 900px; overflow: hidden; }
  body {
    background: var(--bg);
    font-family: "Arimo", Arial, sans-serif;
    position: relative;
  }
  .card {
    position: absolute;
    left: 270px;
    width: 660px;
    height: 377px;
    border-radius: 28px;
    background: linear-gradient(135deg, var(--card-edge) 0%, var(--card) 55%, #050505 100%);
    box-shadow: 0 18px 40px rgba(0,0,0,.55);
    overflow: hidden;
  }
  .card--back { top: 40px; }
  .card--front { top: 470px; }

  .star-field {
    position: absolute;
    left: 0; top: 0;
    width: 55%; height: 100%;
    background: radial-gradient(ellipse at 30% 60%, rgba(60,60,60,.35) 0%, rgba(30,30,30,.15) 45%, rgba(0,0,0,0) 75%);
  }
  .card--front .star-field { width: 40%; height: 60%; }

  .brand {
    position: absolute;
    display: flex;
    align-items: center;
    gap: 10px;
    color: var(--white);
    font-weight: 400;
    font-size: 22px;
    letter-spacing: 3px;
    text-transform: uppercase;
    white-space: nowrap;
  }
  .brand__mark { width: 14px; height: 14px; background: var(--red); flex: none; }
  .card--back .brand { right: 70px; top: 170px; }
  .card--front .brand { right: 50px; top: 62px; font-size: 20px; }

  .holder { position: absolute; left: 48px; top: 150px; }
  .holder__name { color: var(--red); font-weight: 700; font-size: 30px; line-height: 1.1; }
  .holder__title { color: var(--white); font-size: 21px; margin-top: 2px; }

  .divider {
    position: absolute;
    left: 48px; right: 60px; top: 230px;
    height: 2px;
    background: var(--white);
  }

  .contacts { position: absolute; left: 48px; top: 248px; list-style: none; }
  .contacts li {
    display: flex; align-items: center; gap: 12px;
    color: var(--white); font-size: 21px; height: 33px;
  }
  .contacts svg { width: 26px; height: 26px; flex: none; }

  .location {
    position: absolute; right: 60px; top: 246px;
    color: var(--white); font-size: 21px;
  }
</style>
</head>
<body>
  <section class="card card--back" aria-label="Card back">
    <div class="star-field" role="img" aria-label="Faint scattered star pattern"></div>
    <div class="brand"><span class="brand__mark"></span>Ironmark Framing Texas</div>
  </section>

  <section class="card card--front" aria-label="Card front">
    <div class="star-field" role="img" aria-label="Faint scattered star pattern"></div>
    <div class="brand"><span class="brand__mark"></span>Ironmark Framing Texas</div>

    <div class="holder">
      <p class="holder__name">Wesley Corman</p>
      <p class="holder__title">President</p>
    </div>

    <div class="divider"></div>

    <ul class="contacts">
      <li>
        <svg viewBox="0 0 26 26" aria-hidden="true"><rect width="26" height="26" rx="6" fill="var(--red)"/><path d="M8 6.5c1-.6 1.8 0 2.4 1.2l.8 1.7c.3.8 0 1.3-.6 1.8-.5.4-.5.9-.1 1.6.9 1.5 2 2.6 3.5 3.4.6.4 1.1.3 1.5-.2.5-.6 1-.9 1.8-.5l1.7.8c1.2.6 1.7 1.4 1 2.4-1.2 1.7-3.3 1.8-5.6.4-3-1.8-5.4-4.3-6.9-7.4C6.8 9.6 6.6 7.5 8 6.5z" fill="var(--white)"/></svg>
        254-617-0382
      </li>
      <li>
        <svg viewBox="0 0 26 26" aria-hidden="true"><rect width="26" height="26" rx="6" fill="var(--red)"/><rect x="6" y="8" width="14" height="10" fill="none" stroke="var(--white)" stroke-width="1.6"/><path d="M6 8l7 6 7-6M6 18l5-5M20 18l-5-5" fill="none" stroke="var(--white)" stroke-width="1.6"/></svg>
        wesley@ironmarkframing.com
      </li>
      <li>
        <svg viewBox="0 0 26 26" aria-hidden="true"><rect width="26" height="26" rx="6" fill="var(--red)"/><circle cx="13" cy="13" r="7" fill="none" stroke="var(--white)" stroke-width="1.6"/><ellipse cx="13" cy="13" rx="3" ry="7" fill="none" stroke="var(--white)" stroke-width="1.4"/><path d="M6 13h14" stroke="var(--white)" stroke-width="1.4"/></svg>
        www.ironmarkframing.com
      </li>
    </ul>

    <p class="location">Cedar Knoll, TX</p>
  </section>
</body>
</html>
```